Modern business card for triathlon training business in Australia

We need a business card design for our triathlon training company.

Pace with Us Fitness is an Australian business, owned by women, run for women. Pace with Us Fitness helps women prepare or improve triathlon skills and confidence through triathlon camps completely designed for women.

Our camps focus on preparing women both physically and mentally for their next (or first!) triathlon.

You can see our website www.pacewithusfitness.com.au for more info about our business and our style.

We've attached two of our logos and are happy to consider a design that utilised either colour scheme with the teal colour being our 'feature' colour. We don't want overly feminine cards but rather cards that are professional and neat. If the inclusion of any pictures/art is warranted, this should be focused on our swim/ride/run theme and in that specific order (swim/ride/run).

The business card needs to be a printable design and the contact details will need to change for our two employees.

Target Market(s)

Female clients and partners/vendors/sponsors that we work with in the triathlon industry

Industry/Entity Type

Fitness

Contact Information for Business Card

Pace with Us Fitness (business name)
Nina Carver
Business Director
Mobile: 0438 916 207
Email: nina@pacewithusfitness.com.au
www.pacewithusfitness.com.au

Second business card:
Pace with Us Fitness
Bel Stray
Coaching Director
Mobile: 0459 260 718
Email: bel@pacewithusfitness.com.au

Font styles to use
Serif
Sans Serif

Requirements
Must have
• Core contact details above, our logo and be a printable design
Should not have
• Pink
• Cursive/script fonts

```html
<!DOCTYPE html>
<html lang="en">
<head>
<meta charset="utf-8">
<title>Pace with Us Fitness — Business Cards</title>
<link rel="stylesheet" href="https://fonts.googleapis.com/css2?family=Didact+Gothic&family=Open+Sans:wght@300;400;600;700&display=swap">
<style>
  :root {
    --backdrop: #e9eaeb;
    --teal-light: #1cbdcd;
    --teal-main: #0db4c7;
    --teal-deep: #0a9fb1;
    --teal-shade: #12a9ba;
    --white: #ffffff;
  }
  * { box-sizing: border-box; margin: 0; padding: 0; }
  html, body {
    width: 1200px; height: 1200px; overflow: hidden;
    background: var(--backdrop);
  }
  .sheet { position: relative; width: 1200px; height: 1200px; }
  .card {
    position: absolute; left: 263px;
    width: 674px; height: 440px;
    background: var(--teal-main);
    color: var(--white);
    font-family: "Open Sans", sans-serif;
    overflow: hidden;
  }
  .card--bel { top: 108px; }
  .card--nina { top: 650px; }
  .card__brand-panel {
    position: absolute; left: 0; top: 0; bottom: 0; width: 274px;
    background: var(--teal-light);
    border-right: 1px solid var(--teal-deep);
  }
  .brand {
    position: absolute; left: 56px; top: 150px; width: 170px;
    font-family: "Open Sans", sans-serif; font-weight: 700;
    font-size: 30px; line-height: 1.08; letter-spacing: -0.5px;
    color: var(--white);
  }
  .discipline-art {
    position: absolute; left: 275px; top: 50px; width: 90px; height: 330px;
    background: linear-gradient(180deg, var(--teal-shade), var(--teal-main));
    opacity: 0.85;
  }
  .person {
    position: absolute; right: 42px; top: 78px; text-align: right;
  }
  .person__name {
    font-family: "Didact Gothic", sans-serif;
    font-size: 52px; line-height: 1; letter-spacing: 0.5px;
  }
  .person__role {
    margin-top: 10px;
    font-weight: 300; font-size: 19px;
  }
  .contacts {
    position: absolute; left: 400px; top: 254px; list-style: none;
  }
  .contact {
    display: flex; align-items: center; gap: 8px;
    height: 20px; margin-bottom: 14px;
    font-weight: 700; font-size: 11px; letter-spacing: 2px;
  }
  .contact--phone { font-size: 14px; letter-spacing: 3px; }
  .contact__icon { width: 17px; height: 17px; flex: none; }
</style>
</head>
<body>
<main class="sheet">

  <section class="card card--bel">
    <div class="card__brand-panel">
      <p class="brand">Pace with Us Fitness</p>
    </div>
    <div class="discipline-art" role="img" aria-label="Embossed silhouettes of a swimmer, cyclist and runner in sequence"></div>
    <header class="person">
      <h1 class="person__name">Bel Stray</h1>
      <p class="person__role">Coaching Director</p>
    </header>
    <ul class="contacts">
      <li class="contact contact--phone">
        <svg class="contact__icon" viewBox="0 0 20 20" fill="none" stroke="#fff" stroke-width="1.5"><circle cx="10" cy="10" r="8.5"/><path d="M7 5.5l1.5 2.2-1 1.2c.6 1.3 1.6 2.3 2.9 2.9l1.2-1 2.2 1.5-.8 1.6c-3.4-.2-6.6-3.4-6.8-6.8z" fill="#fff" stroke="none"/></svg>
        0459 260 718
      </li>
      <li class="contact">
        <svg class="contact__icon" viewBox="0 0 20 20" fill="none" stroke="#fff" stroke-width="1.5"><circle cx="10" cy="10" r="8.5"/><rect x="5.5" y="7" width="9" height="6.5"/><path d="M5.5 7l4.5 3.5L14.5 7"/></svg>
        bel@pacewithusfitness.com.au
      </li>
      <li class="contact">
        <svg class="contact__icon" viewBox="0 0 20 20" fill="none" stroke="#fff" stroke-width="1.3"><circle cx="10" cy="10" r="8.5"/><ellipse cx="10" cy="10" rx="3.8" ry="8.5"/><path d="M1.5 10h17M3 6h14M3 14h14"/></svg>
        www.pacewithusfitness.com.au
      </li>
    </ul>
  </section>

  <section class="card card--nina">
    <div class="card__brand-panel">
      <p class="brand">Pace with Us Fitness</p>
    </div>
    <div class="discipline-art" role="img" aria-label="Embossed silhouettes of a swimmer, cyclist and runner in sequence"></div>
    <header class="person">
      <h1 class="person__name">Nina Carver</h1>
      <p class="person__role">Business Director</p>
    </header>
    <ul class="contacts">
      <li class="contact contact--phone">
        <svg class="contact__icon" viewBox="0 0 20 20" fill="none" stroke="#fff" stroke-width="1.5"><circle cx="10" cy="10" r="8.5"/><path d="M7 5.5l1.5 2.2-1 1.2c.6 1.3 1.6 2.3 2.9 2.9l1.2-1 2.2 1.5-.8 1.6c-3.4-.2-6.6-3.4-6.8-6.8z" fill="#fff" stroke="none"/></svg>
        0438 916 207
      </li>
      <li class="contact">
        <svg class="contact__icon" viewBox="0 0 20 20" fill="none" stroke="#fff" stroke-width="1.5"><circle cx="10" cy="10" r="8.5"/><rect x="5.5" y="7" width="9" height="6.5"/><path d="M5.5 7l4.5 3.5L14.5 7"/></svg>
        nina@pacewithusfitness.com.au
      </li>
      <li class="contact">
        <svg class="contact__icon" viewBox="0 0 20 20" fill="none" stroke="#fff" stroke-width="1.3"><circle cx="10" cy="10" r="8.5"/><ellipse cx="10" cy="10" rx="3.8" ry="8.5"/><path d="M1.5 10h17M3 6h14M3 14h14"/></svg>
        www.pacewithusfitness.com.au
      </li>
    </ul>
  </section>

</main>
</body>
</html>
```